PLOVEN Business Card

Coastal Build Additions and Refits. I need a business card designed for this new high end renovation business. I would like the logo centered on the back side with the ABN (37 915 402 176) on the bottom right hand corner.

I would like the following information placed on the other side along with some customized pattern or design.

Derek Collwood
Director
Phone: 1300 480 957
Fax: (02) 8145 9021
Website: www.plovenbuilders.com.au
Email: d.collwood@plovenbuilders.com.au
PO Box 87,
Kelvinbrook NSW 2069

(FB Logo) PLOVEN - Coastal Build Additions and Refits

The final design should communicate professionalism and trust.

Back side background colour: white
Front side: Undecided

```html
<!DOCTYPE html>
<html lang="en">
<head>
<meta charset="utf-8">
<title>PLOVEN Business Card</title>
<link rel="stylesheet" href="https://fonts.googleapis.com/css2?family=Cinzel:wght@600&family=Open+Sans:wght@400;600;700&display=swap">
<style>
  :root {
    --page: #e4e5e7;
    --card: #ffffff;
    --navy: #0b3f86;
    --navy-deep: #082a5e;
    --ink: #2b2f36;
    --brand-blue: #15549e;
    --white: #ffffff;
  }
  * { margin: 0; padding: 0; box-sizing: border-box; }
  html, body { width: 1200px; height: 861px; overflow: hidden; }
  body {
    background: var(--page);
    font-family: "Open Sans", Arial, sans-serif;
    position: relative;
  }
  .card {
    position: absolute;
    top: 265px;
    width: 540px;
    height: 330px;
    background: var(--card);
    box-shadow: 0 6px 18px rgba(0,0,0,0.18);
    overflow: hidden;
  }
  .card--front { left: 40px; }
  .card--back { left: 620px; }

  .band { position: absolute; inset: 0; }

  .logo {
    position: absolute;
    text-align: center;
    color: var(--ink);
  }
  .logo__name {
    font-family: "Cinzel", Georgia, serif;
    font-weight: 600;
    color: var(--ink);
    letter-spacing: 2px;
    line-height: 1;
  }
  .logo__tagline {
    display: flex;
    align-items: center;
    gap: 8px;
    font-family: "Cinzel", Georgia, serif;
    font-weight: 600;
    color: var(--brand-blue);
    white-space: nowrap;
  }
  .logo__tagline::before,
  .logo__tagline::after {
    content: "";
    flex: 1;
    height: 2px;
    background: var(--brand-blue);
  }

  .card--front .logo { left: 60px; top: 30px; width: 360px; }
  .card--front .logo__name { font-size: 50px; }
  .card--front .logo__tagline { font-size: 12px; margin-top: 4px; }

  .card--back .logo { left: 70px; top: 92px; width: 400px; }
  .card--back .logo__name { font-size: 62px; }
  .card--back .logo__tagline { font-size: 14px; margin-top: 6px; }

  .contacts {
    position: absolute;
    left: 22px;
    top: 160px;
    list-style: none;
    color: var(--white);
    font-size: 12px;
    font-weight: 600;
  }
  .contacts__item {
    display: flex;
    align-items: center;
    gap: 7px;
    height: 21px;
  }
  .contacts__icon { width: 15px; height: 15px; flex: none; }

  .person {
    position: absolute;
    right: 26px;
    bottom: 44px;
    text-align: right;
    color: var(--white);
  }
  .person__name { font-size: 25px; font-weight: 700; line-height: 1.1; }
  .person__role { font-size: 15px; font-weight: 400; }

  .abn {
    position: absolute;
    right: 30px;
    bottom: 34px;
    font-size: 14px;
    font-weight: 700;
    color: var(--ink);
    letter-spacing: 0.5px;
  }
</style>
</head>
<body>

<section class="card card--front" aria-label="Card front">
  <svg class="band" viewBox="0 0 540 330" preserveAspectRatio="none" aria-hidden="true">
    <defs>
      <linearGradient id="bandFill" x1="0" y1="0" x2="0" y2="1">
        <stop offset="0" stop-color="var(--navy)"/>
        <stop offset="1" stop-color="var(--navy-deep)"/>
      </linearGradient>
    </defs>
    <path d="M0,140 Q280,88 540,126 L540,330 L0,330 Z" fill="url(#bandFill)"/>
  </svg>

  <div class="logo">
    <div class="logo__name">PLOVEN</div>
    <div class="logo__tagline">Coastal Build Additions &amp; Refits</div>
  </div>

  <ul class="contacts">
    <li class="contacts__item">
      <svg class="contacts__icon" viewBox="0 0 16 16"><circle cx="8" cy="8" r="8" fill="#fff"/><path d="M5.2 4h1.6l.7 2-1 .8a5 5 0 0 0 2.7 2.7l.8-1 2 .7v1.6c0 .5-.4.9-.9.9A7 7 0 0 1 4.3 4.9c0-.5.4-.9.9-.9z" fill="var(--navy)"/></svg>
      <span>1300 480 957</span>
    </li>
    <li class="contacts__item">
      <svg class="contacts__icon" viewBox="0 0 16 16"><circle cx="8" cy="8" r="8" fill="#fff"/><rect x="5" y="3.5" width="6" height="3" fill="var(--navy)"/><rect x="3.5" y="6.5" width="9" height="4" rx="1" fill="var(--navy)"/><rect x="5" y="10" width="6" height="2.5" fill="var(--navy)"/></svg>
      <span>(02) 8145 9021</span>
    </li>
    <li class="contacts__item">
      <svg class="contacts__icon" viewBox="0 0 16 16"><circle cx="8" cy="8" r="8" fill="#fff"/><g fill="none" stroke="var(--navy)" stroke-width="1"><circle cx="8" cy="8" r="4.5"/><ellipse cx="8" cy="8" rx="2" ry="4.5"/><path d="M3.5 8h9"/></g></svg>
      <span>www.plovenbuilders.com.au</span>
    </li>
    <li class="contacts__item">
      <svg class="contacts__icon" viewBox="0 0 16 16"><circle cx="8" cy="8" r="8" fill="#fff"/><rect x="3.8" y="5" width="8.4" height="6" fill="var(--navy)"/><path d="M3.8 5l4.2 3.4L12.2 5" fill="none" stroke="#fff" stroke-width="0.9"/></svg>
      <span>d.collwood@plovenbuilders.com.au</span>
    </li>
    <li class="contacts__item">
      <svg class="contacts__icon" viewBox="0 0 16 16"><circle cx="8" cy="8" r="8" fill="#fff"/><path d="M8 3.3a3 3 0 0 1 3 3c0 2.2-3 6.2-3 6.2S5 8.5 5 6.3a3 3 0 0 1 3-3z" fill="var(--navy)"/><circle cx="8" cy="6.3" r="1.1" fill="#fff"/></svg>
      <span>PO Box 87, Kelvinbrook NSW 2069</span>
    </li>
    <li class="contacts__item">
      <svg class="contacts__icon" viewBox="0 0 16 16"><circle cx="8" cy="8" r="8" fill="#fff"/></svg>
      <span>PLOVEN - Coastal Build Additions and Refits</span>
    </li>
  </ul>

  <div class="person">
    <div class="person__name">Derek Collwood</div>
    <div class="person__role">Director</div>
  </div>
</section>

<section class="card card--back" aria-label="Card back">
  <div class="logo">
    <div class="logo__name">PLOVEN</div>
    <div class="logo__tagline">Coastal Build Additions &amp; Refits</div>
  </div>
  <div class="abn">ABN 37 915 402 176</div>
</section>

</body>
</html>
```